Need 8.5" x 11" as well as large 11"x17" Posters for our upcoming event

Please include LOGOs in poster
Main logo is Harborview Teen Circle of PL

All high school age faith groups are invited to come and join with 150 to 175 other high school students from various faith traditions to participate in the Harborview Teen Circle of Pine Lakes‘s Annual Kindred Voices Gathering. More than ever, our county and world need young leaders who are willing to learn from each other and build stronger communities!

KINDRED GATHERING
The purpose of this Interfaith Youth Forum is to bring together young people from diverse ethnic, cultural, and religious backgrounds, and to engage them in dialogue. True dialogue is a conversation on a common subject between two or more persons of differing points of view and/or backgrounds. We feel that this commitment to dialogue will affect relationships in a constructive way in our places of worship and in our community.
The forum itself involves having eight religiously diverse high school-age students, one adult, and youth leader around each table to discuss common questions. Our youth leaders act as facilitators, but it is stressed that it is the students we want to hear from.
RSVP for our KINDRED GATHERING before February 18th, 2018
FORUM QUESTIONS Available online at http://htcpl-example.org/home/kindred-fair/

Target Market(s)

Houses of worship, community leaders, High School Students

Industry/Entity Type

Non-Profit

Font styles to use
Serif

Colors
cfdeed
0255a3
f78f20
f37122
f68d4d
faa54b
ffcf3e
ffc214
34a6d7

Requirements
Must have
• Harborview Teen Circle of Pine Lakes's 14th Annual Kindred Gathering & Fair
• TEENS EXPRESSING THEIR FAITH THROUGH ART, MUSIC, AND DIALOGUE
• THIS YEAR'S THEME: “Who Are You?”
• Sunday, March 11th, 2018 11:00am-5:00pm
• Congregation Ner Adamah
• 4187 W Larkmont Rd. Santa Ana, CA 92705
• Email: htcplorg@mailbox-example.com
• Website: HTCPL-example.org
• Facebook: Harborview Teen Circle of Pine Lakes
Nice to have
• Descriptions provided in word doc
Should not have
• -

```html
<!DOCTYPE html>
<html lang="en">
<head>
<meta charset="utf-8">
<title>Interfaith Youth Forum – Kindred Gathering &amp; Fair</title>
<link rel="stylesheet" href="https://fonts.googleapis.com/css2?family=Oswald:wght@400;500;600&family=Tinos:wght@400;700&family=Raleway:wght@400;500&display=swap">
<style>
:root{
  --navy:#2b4f8a;
  --panel:#2f5f98;
  --deep:#1f3f7a;
  --sky:#58bdf0;
  --cyan:#34a6d7;
  --orange:#f78f20;
  --venue:#f37122;
  --gold:#faa54b;
  --sun:#ffc214;
  --yellow:#ffcf3e;
  --pale:#cfdeed;
  --ink:#333;
  --white:#fff;
}
*{margin:0;padding:0;box-sizing:border-box}
html,body{width:1200px;height:1200px;overflow:hidden;background:#ececec}
.stage{position:relative;width:1200px;height:1200px}
.poster-frame{position:absolute;left:138px;top:0;width:924px;height:1200px;overflow:hidden}
.poster{position:absolute;left:0;top:0;width:1023px;height:1328px;transform:scale(0.9036);transform-origin:0 0;
  background:linear-gradient(180deg,#fff 0%,#f3f3f3 60%,#e6e6e6 100%);overflow:hidden;font-family:"Tinos",serif}
.abs{position:absolute}
.header-art{position:absolute;left:0;top:0}
.council-mark{position:absolute;left:106px;top:56px;width:200px;height:200px;border:3px solid var(--white);border-radius:50%;
  display:flex;align-items:center;justify-content:center;text-align:center;color:var(--white);
  font-family:"Tinos",serif;font-weight:700;font-size:19px;line-height:1.25;padding:28px}
.kicker{left:346px;top:28px;color:var(--gold);font-size:26px;font-family:"Tinos",serif}
.tagline{left:346px;top:68px;color:var(--white);font-family:"Raleway",sans-serif;font-size:24px;line-height:35px;letter-spacing:.3px}
.headline{left:343px;top:138px;color:var(--sun);font-family:"Oswald",sans-serif;font-weight:600;font-size:62px;line-height:1;letter-spacing:-.5px}
.theme{left:346px;top:208px;font-size:26px;color:var(--gold)}
.theme q{color:var(--white)}
.intro{left:68px;top:412px;width:555px;font-size:15px;line-height:24.6px;color:var(--ink)}
.divider{left:640px;top:398px;width:2px;height:131px;background:var(--navy)}
.when{right:46px;top:390px;width:325px;text-align:right;font-family:"Oswald",sans-serif;color:var(--navy)}
.when .day{font-size:22px;font-weight:500}
.when .day b{font-size:31px;font-weight:500}
.when .day sup{font-size:11px}
.when .time{font-size:20px;margin-top:2px}
.when .venue{font-size:29px;color:var(--venue);line-height:1.3;font-weight:500;white-space:nowrap}
.when .addr{font-size:13.5px;margin-top:2px;white-space:nowrap}
.strip{left:63px;top:551px;width:913px;height:220px}
.strip .bar{position:absolute;left:0;width:100%;display:flex}
.strip .bar.top{top:0;height:15px}
.strip .bar.bottom{bottom:0;height:20px}
.strip .bar span{display:block;height:100%}
.strip .photos{position:absolute;left:0;top:15px;width:100%;height:185px;display:flex}
.strip .photos div{height:100%}
.s1{width:380px}.s2{width:123px}.s3{width:125px}.s4{width:125px}.s5{width:160px}
.photo-dance{background:linear-gradient(180deg,#3a2e2a 0%,#5a4438 55%,#a26a3c 100%)}
.photo-art{background:linear-gradient(160deg,#6e6a66,#3c3a3c 60%,#8a7a5a)}
.photo-drums{background:linear-gradient(180deg,#cbc6bd,#7a4a2f 70%,#4a2818)}
.photo-music{background:linear-gradient(160deg,#bdb6ae,#6a5a58 60%,#2c2a2e)}
.photo-sitar{background:linear-gradient(160deg,#d6d0c8,#b89a8a 50%,#8a4a32)}
.forum-band{left:63px;top:771px;width:913px;height:142px;background:var(--panel)}
.forum-col{left:63px;top:771px;width:244px;height:557px;background:var(--panel)}
.section-title{font-family:"Oswald",sans-serif;font-weight:600;color:var(--white);line-height:1;letter-spacing:-.3px}
.forum-title{left:70px;top:784px;width:230px;font-size:31px;line-height:1.02;text-align:center}
.forum-title span{color:var(--sky)}
.rsvp{font-family:"Oswald",sans-serif;color:var(--white);text-align:center}
.rsvp .label{font-size:12px;letter-spacing:-.2px}
.rsvp .date{font-size:21px;line-height:1.2}
.forum-rsvp{left:63px;top:856px;width:244px}
.forum-q{left:63px;top:910px;width:244px}
.forum-q .date{font-size:13px;line-height:1.3;word-break:break-all;padding:0 6px}
.photo-circle{left:73px;top:968px;width:221px;height:165px;background:linear-gradient(170deg,#d8d2c6 0%,#5b5656 45%,#2c2c34 100%)}
.forum-text{left:328px;top:781px;width:635px;color:var(--white);font-size:13.4px;line-height:15.2px}
.forum-text p+p{margin-top:13px}
.festival{left:325px;top:919px;width:287px;height:409px;background:var(--panel)}
.festival-title{left:345px;top:938px;font-size:44px}
.festival-title span,.gallery-title span{color:var(--sun)}
.gallery-title span{color:var(--orange)}
.festival-text{left:346px;top:998px;width:255px;color:var(--white);font-size:13.4px;line-height:15.3px}
.festival-rsvp{left:388px;top:1145px;text-align:left}
.festival-rsvp .date{font-size:21px;line-height:1.35}
.gallery{left:631px;top:919px;width:345px;height:224px;background:var(--panel)}
.gallery-title{left:655px;top:936px;font-size:44px}
.gallery-text{left:657px;top:994px;width:310px;color:var(--white);font-size:13.4px;line-height:15.3px}
.gallery-rsvp{left:657px;top:1085px;text-align:left}
.info{left:631px;top:1143px;width:345px;height:87px;background:var(--sun);font-family:"Oswald",sans-serif;color:var(--navy)}
.info .label{position:absolute;left:22px;top:16px;font-size:13px;line-height:14px}
.info ul{position:absolute;left:99px;top:8px;list-style:none;font-size:13.5px;line-height:20.5px}
.info li{display:flex;align-items:center;gap:7px;white-space:nowrap}
.info svg{flex:none}
.sponsor{display:flex;align-items:center;gap:6px;font-family:"Tinos",serif}
.sponsor-a{left:664px;top:1250px;color:var(--navy);font-size:19px;line-height:1}
.sponsor-b{left:828px;top:1258px;color:var(--orange);font-size:13px;line-height:1.2}
.sponsor-b small{display:block;font-size:9.5px}
.ring{width:32px;height:32px;border:2px solid var(--navy);border-radius:50%;flex:none}
.dot{width:14px;height:14px;background:#3e8f4a;flex:none}
.deco{position:absolute}
</style>
</head>
<body>
<div class="stage">
 <div class="poster-frame">
  <main class="poster">

   <svg class="header-art" width="1023" height="400" viewBox="0 0 1023 400" aria-hidden="true">
    <defs>
     <linearGradient id="skyGrad" x1="0" y1="0" x2="1" y2="0.5">
      <stop offset="0" stop-color="#5cc1f2"/>
      <stop offset="0.45" stop-color="#2f74b8"/>
      <stop offset="1" stop-color="#24508f"/>
     </linearGradient>
     <linearGradient id="swoosh" x1="0" x2="1">
      <stop offset="0" stop-color="#f7a21e"/>
      <stop offset="1" stop-color="#f7c23a"/>
     </linearGradient>
    </defs>
    <path d="M0 250 C180 360 470 395 800 350 C620 400 300 410 0 335 Z" fill="url(#swoosh)"/>
    <path d="M470 375 C700 335 880 325 1023 330 V385 C860 345 690 352 470 375 Z" fill="#f5e7a6"/>
    <path d="M0 175 C260 330 690 335 1023 330 V362 C690 352 280 355 0 245 Z" fill="#33357e"/>
    <path d="M0 160 C280 305 690 315 1023 300 V345 C690 330 260 325 0 215 Z" fill="#48c6f2"/>
    <path d="M0 0 H1023 V305 C690 310 270 290 0 160 Z" fill="url(#skyGrad)"/>
   </svg>

   <svg class="deco" style="left:868px;top:0" width="155" height="265" viewBox="0 0 155 265" role="img" aria-label="Faceted geometric decoration in orange, gold and teal">
    <defs>
     <linearGradient id="facetA" x1="0" y1="0" x2="1" y2="1"><stop offset="0" stop-color="#ffcf3e"/><stop offset="1" stop-color="#f37122"/></linearGradient>
    </defs>
    <polygon points="0,80 120,0 155,0 155,265 90,190" fill="url(#facetA)"/>
   </svg>

   <div class="council-mark">Harborview Teen Circle of PL</div>

   <p class="abs kicker">14th Annual Kindred Gathering &amp; Fair</p>
   <p class="abs tagline">TEENS EXPRESSING THEIR FAITH<br>THROUGH ART, MUSIC, AND DIALOGUE</p>
   <h1 class="abs headline">INTERFAITH YOUTH FORUM</h1>
   <p class="abs theme">THIS YEAR'S THEME: <q>Who Are You?</q></p>

   <p class="abs intro">All high school age faith groups are invited to come and join with 150 to 175 other high school students from various faith traditions to participate in the Harborview Teen Circle of Pine Lakes‘s Annual Kindred Voices Gathering.&nbsp; More than ever, our county and world need young leaders who are willing to learn from each other and build stronger communities!</p>
   <div class="abs divider"></div>
   <div class="abs when">
    <p class="day"><b>Sunday,</b> March 11<sup>th</sup>, 2018</p>
    <p class="time">11:00am-5:00pm</p>
    <p class="venue">Congregation Ner Adamah</p>
    <p class="addr">4187 W Larkmont Rd. Santa Ana, CA 92705</p>
   </div>

   <section class="abs strip">
    <div class="bar top"><span class="s1" style="background:#58bdf0"></span><span class="s2" style="background:#33357e"></span><span class="s3" style="background:#f78f20"></span><span class="s4" style="background:#ffcf3e"></span><span class="s5" style="background:#f8e9a6"></span></div>
    <div class="photos">
     <div class="s1 photo-dance" role="img" aria-label="Photo of students performing a dance on stage"></div>
     <div class="s2 photo-art" role="img" aria-label="Photo of hands making sand artwork"></div>
     <div class="s3 photo-drums" role="img" aria-label="Photo of a student playing drums"></div>
     <div class="s4 photo-music" role="img" aria-label="Photo of students singing and playing harmonium"></div>
     <div class="s5 photo-sitar" role="img" aria-label="Photo of a student playing sitar"></div>
    </div>
    <div class="bar bottom"><span class="s1" style="background:#58bdf0"></span><span class="s2" style="background:#33357e"></span><span class="s3" style="background:#f78f20"></span><span class="s4" style="background:#ffcf3e"></span><span class="s5" style="background:#f8e9a6"></span></div>
   </section>

   <div class="abs forum-band"></div>
   <div class="abs forum-col"></div>
   <h2 class="abs section-title forum-title">KINDRED<br><span>GATHERING</span></h2>
   <div class="abs rsvp forum-rsvp"><p class="label">RSVP for our KINDRED GATHERING</p><p class="date">before February 18th, 2018</p></div>
   <div class="abs rsvp forum-q"><p class="label">FORUM QUESTIONS</p><p class="date">at http://htcpl-example.org/home/kindred-fair/</p></div>
   <div class="abs photo-circle" role="img" aria-label="Photo of students seated together in a dialogue session"></div>
   <div class="abs forum-text">
    <p>The purpose of this Interfaith Youth Forum is to bring together young people from diverse ethnic, cultural, and religious backgrounds, and to engage them in dialogue.&nbsp; True dialogue is a conversation on a common subject between two or more persons of differing points of view and/or backgrounds.&nbsp; We feel that this commitment to dialogue will affect relationships in a constructive way in our places of worship and in our community.</p>
    <p>The forum itself involves having eight religiously diverse high school-age students, one adult, and youth leader around each table to discuss common questions.&nbsp; Our youth leaders act as facilitators, but it is stressed that it is the students we want to hear from.</p>
   </div>

   <div class="abs festival"></div>
   <h2 class="abs section-title festival-title">FAITH <span>FESTIVAL</span></h2>
   <p class="abs festival-text">The forum will include our Faith Festival portion of the program which families of the participants are welcomed to join.&nbsp; The Festival will include musical performances of all types from diverse religious communities.&nbsp; The differing performing arts include but are not limited to singing, dancing, instrumental music, storytelling, etc.</p>
   <div class="abs rsvp festival-rsvp"><p class="label">RSVP for our FAITH FESTIVAL</p><p class="date">by February 11th, 2018<br>(Music, Song, Dance)</p></div>

   <div class="abs gallery"></div>
   <h2 class="abs section-title gallery-title">ART <span>GALLERY</span></h2>
   <p class="abs gallery-text">This event will include and Art Gallery display of students' work, highlighting their expressions of faith, and artwork promoting learning, understanding, leadership, and service.&nbsp; Art includes any painting, illustration, sculpture, photography or other visual art.</p>
   <div class="abs rsvp gallery-rsvp"><p class="label">Art Work for our Art Gallery must be submitted</p><p class="date">by March 3rd, 2018</p></div>

   <div class="abs info">
    <p class="label">Further<br>Information :</p>
    <ul>
     <li><svg width="14" height="11" viewBox="0 0 14 11"><rect x="0.7" y="0.7" width="12.6" height="9.6" fill="none" stroke="#2b4f8a" stroke-width="1.2"/><path d="M1 1 L7 6 L13 1" fill="none" stroke="#2b4f8a" stroke-width="1.2"/></svg>htcplorg@mailbox-example.com</li>
     <li><svg width="14" height="14" viewBox="0 0 14 14"><circle cx="7" cy="7" r="6" fill="none" stroke="#2b4f8a" stroke-width="1.2"/><ellipse cx="7" cy="7" rx="2.6" ry="6" fill="none" stroke="#2b4f8a" stroke-width="1"/><path d="M1 7 H13" stroke="#2b4f8a" stroke-width="1"/></svg>HTCPL-example.org</li>
     <li><svg width="13" height="13" viewBox="0 0 13 13"><rect width="13" height="13" rx="2" fill="#2b4f8a"/></svg>Harborview Teen Circle of Pine Lakes</li>
    </ul>
   </div>

   <div class="abs sponsor sponsor-a"><span>Fresh Horizon<br>Allies</span><span class="ring"></span></div>
   <div class="abs sponsor sponsor-b"><span class="dot"></span><span>Congregation Ner Adamah<small>www.NerAdamah-example.org</small></span></div>

   <svg class="deco" style="left:0;top:1160px" width="670" height="168" viewBox="0 0 670 168" role="img" aria-label="Faceted geometric decoration in orange, red and teal">
    <defs>
     <linearGradient id="facetB" x1="0" y1="0" x2="1" y2="0"><stop offset="0" stop-color="#c44a1a"/><stop offset="0.35" stop-color="#f78f20"/><stop offset="0.55" stop-color="#34a6d7"/><stop offset="0.8" stop-color="#2d4f9a"/><stop offset="1" stop-color="#7fe0e0"/></linearGradient>
    </defs>
    <polygon points="0,20 120,40 230,0 330,120 440,60 560,70 660,168 0,168" fill="url(#facetB)"/>
   </svg>

  </main>
 </div>
</div>
</body>
</html>
```